Biz Card for Harrowfield Property Partners - HFPP

Harrowfield Property Partners is a commercial real estate acquisitions firm. We buy commercial property and need to raise capital from investors for each deal we buy. The vibe needs to be: give us your money, we will multiply it.
Our website: www.hfldpp.com
Competitors are: https://marvenby.com/, https://trellumpartners.com/, http://www.quorvantcapital.com/
Target Market(s)
High Net Worth Individuals, Bankers, Insurance Companies, Commercial Real Estate Brokers.
Industry/Entity Type
Investment Banking
Contact Information for Business Card
Name, Title, Addess, Cell#, Office#, email, website
Requirements
Must have
- use one of our logos. See website for look and feel: www.hfldpp.com
Nice to have
- see website: www.hfldpp.com

```html
<!DOCTYPE html>
<html lang="en">
<head>
<meta charset="utf-8">
<title>Harrowfield Property Partners – Business Card</title>
<link href="https://fonts.googleapis.com/css2?family=Montserrat:wght@300;400;700&display=swap" rel="stylesheet">
<style>
  :root {
    --navy: #0b2440;
    --navy-soft: #12304f;
    --white: #ffffff;
    --backdrop: #6e7073;
  }
  * { margin: 0; padding: 0; box-sizing: border-box; }
  html, body { width: 1200px; height: 965px; overflow: hidden; }
  body {
    background: var(--backdrop);
    font-family: "Montserrat", Arial, sans-serif;
    color: var(--white);
    display: flex;
    flex-direction: column;
    align-items: center;
    justify-content: center;
    gap: 44px;
  }
  .card {
    position: relative;
    width: 700px;
    height: 400px;
    background: var(--navy);
    overflow: hidden;
    box-shadow: 0 10px 26px rgba(0,0,0,0.35);
  }
  .brand {
    position: absolute;
    display: flex;
    align-items: center;
    gap: 22px;
  }
  .brand-dot {
    border-radius: 50%;
    background: var(--white);
    flex: none;
  }
  .brand-name { font-weight: 300; color: var(--white); line-height: 1; }
  .brand-name .line-main { display: block; letter-spacing: 0.22em; }
  .brand-name .line-sub { display: block; letter-spacing: 0.32em; margin-top: 10px; }

  /* front */
  .card-front .brand { left: 80px; top: 150px; }
  .card-front .brand-dot { width: 100px; height: 100px; }
  .card-front .line-main { font-size: 40px; }
  .card-front .line-sub { font-size: 14px; }
  .front-halo {
    position: absolute;
    left: 170px; top: 30px;
    width: 340px; height: 340px;
    border-radius: 50%;
    background: var(--navy-soft);
    box-shadow: inset 0 2px 4px rgba(0,0,0,0.35), 0 1px 0 rgba(255,255,255,0.05);
  }

  /* back */
  .card-back .brand { left: 42px; top: 40px; }
  .card-back .brand-dot { width: 82px; height: 82px; }
  .card-back .line-main { font-size: 32px; }
  .card-back .line-sub { font-size: 11.5px; margin-top: 8px; }

  .person { position: absolute; left: 44px; top: 190px; }
  .person-name { font-weight: 700; font-size: 24px; letter-spacing: 0.02em; }
  .person-title { font-weight: 400; font-size: 16px; margin-top: 2px; }

  .contact-list { position: absolute; left: 44px; top: 262px; list-style: none; }
  .contact-list li {
    display: flex; align-items: center; gap: 12px;
    font-size: 17px; font-weight: 400; line-height: 27px;
  }
  .contact-list svg { width: 16px; height: 16px; flex: none; }

  .address {
    position: absolute; right: 40px; top: 190px;
    text-align: right; font-size: 16px; line-height: 22px; font-weight: 400;
  }
</style>
</head>
<body>

  <section class="card card-front" aria-label="Card front">
    <div class="front-halo"></div>
    <div class="brand">
      <span class="brand-dot"></span>
      <span class="brand-name">
        <span class="line-main">HARROWFIELD</span>
        <span class="line-sub">PROPERTY PARTNERS</span>
      </span>
    </div>
  </section>

  <section class="card card-back" aria-label="Card back">
    <div class="brand">
      <span class="brand-dot"></span>
      <span class="brand-name">
        <span class="line-main">HARROWFIELD</span>
        <span class="line-sub">PROPERTY PARTNERS</span>
      </span>
    </div>

    <div class="person">
      <p class="person-name">DANIEL M. OSTROVA</p>
      <p class="person-title">Managing Partner Multifamily</p>
    </div>

    <ul class="contact-list">
      <li>
        <svg viewBox="0 0 16 16" fill="none" stroke="#fff" stroke-width="1.3"><rect x="4" y="1" width="8" height="14" rx="1.5"/><line x1="7" y1="12.5" x2="9" y2="12.5"/></svg>
        (000) 000-0000
      </li>
      <li>
        <svg viewBox="0 0 16 16" fill="none" stroke="#fff" stroke-width="1.3"><path d="M3 2h3l1.5 3.5-2 1.3a8 8 0 0 0 3.7 3.7l1.3-2L14 10v3a1.5 1.5 0 0 1-1.5 1.5A11.5 11.5 0 0 1 1.5 3.5 1.5 1.5 0 0 1 3 2z"/></svg>
        (000) 000-0000
      </li>
      <li>
        <svg viewBox="0 0 16 16" fill="none" stroke="#fff" stroke-width="1.3"><rect x="1.5" y="3.5" width="13" height="9" rx="1"/><path d="M1.5 4l6.5 5 6.5-5"/></svg>
        info@hfldpp.com
      </li>
      <li>
        <svg viewBox="0 0 16 16" fill="none" stroke="#fff" stroke-width="1.2"><circle cx="8" cy="8" r="6.5"/><ellipse cx="8" cy="8" rx="2.8" ry="6.5"/><line x1="1.5" y1="8" x2="14.5" y2="8"/></svg>
        www.hfldpp.com
      </li>
    </ul>

    <address class="address" style="font-style:normal">
      418 Verandel Ave, Suite 910<br>
      Larkmont, FL 33190
    </address>
  </section>

</body>
</html>
```